The Maple Sprout Clinic needs a Letterhead

We are a bilingual pediatric clinic located in Montreal, Canada.

Our english name is Maple Sprout Clinic
Our french name is Clinique du petit ruisseau

We offer complete care for children including general pediatric care, pediatric specialist care such as Ear, Nose and Throat, Urology, Neurology and Adolescent Medicine. We also have paramedical specialists such as psychologists, social workers, occupational therapists, speech and language pathologists.

The letterhead must use and be harmonious with our new logo. See Design #4923293. We need two types of letterhead. One for a the Logo and both english and french names on the top and the second with the list of current staff on the left. I have uploaded two old examples for you to see. Thanks and good luck.

Font styles to use
Sans Serif

Colors
3176b5
9d9d9d

Requirements
Must have
• Include our logo.
Nice to have
• Most of our printing is done in black and white. So a grayscale design is fine.
I have included a color and grayscale versions of our logo.

We prefer clean modern designs.

```html
<!DOCTYPE html>
<html lang="fr">
<head>
<meta charset="utf-8">
<title>Maple Sprout Clinic – Letterhead</title>
<link rel="stylesheet" href="https://fonts.googleapis.com/css2?family=Questrial&family=Lato:wght@400&display=swap">
<style>
  :root {
    --backdrop: #e6e3df;
    --paper: #ffffff;
    --ink-grey: #7a7a7a;
    --ink-dark: #555555;
    --rule: #8a8a8a;
    --rule-light: #c9c9c9;
    --watermark: #f4f4f4;
  }
  html, body {
    margin: 0;
    padding: 0;
    width: 1115px;
    height: 1200px;
    overflow: hidden;
    background: var(--backdrop);
  }
  .letterhead {
    position: absolute;
    left: 142px;
    top: 13px;
    width: 830px;
    height: 1174px;
    background: var(--paper);
    overflow: hidden;
    box-shadow: 0 1px 4px rgba(0,0,0,0.12);
  }
  .watermark-disc {
    position: absolute;
    left: 350px;
    top: 718px;
    width: 480px;
    height: 480px;
    border-radius: 50%;
    background: var(--watermark);
  }
  .masthead {
    position: absolute;
    top: 24px;
    left: 0;
    right: 0;
    display: flex;
    justify-content: center;
    align-items: center;
    gap: 16px;
    font-family: "Questrial", sans-serif;
    font-size: 22px;
    line-height: 24px;
    color: var(--ink-grey);
  }
  .masthead__name {
    margin: 0;
    font-weight: 400;
    font-size: inherit;
    text-align: center;
    width: 150px;
  }
  .masthead__dot {
    width: 22px;
    height: 22px;
    border-radius: 50%;
    background: var(--ink-grey);
  }
  .rule {
    position: absolute;
    left: 57px;
    right: 58px;
    height: 0;
  }
  .rule--top { top: 130px; border-top: 1px solid var(--rule); }
  .rule--bottom { top: 1115px; border-top: 1px solid var(--rule-light); }
  .contact {
    position: absolute;
    top: 1123px;
    left: 0;
    right: 0;
    text-align: center;
    font-family: "Lato", sans-serif;
    color: var(--ink-dark);
  }
  .contact__address { margin: 0; font-size: 13.5px; line-height: 18px; }
  .contact__lines { margin: 0; font-size: 12px; line-height: 17px; }
</style>
</head>
<body>
  <main class="letterhead">
    <div class="watermark-disc" aria-hidden="true"></div>

    <header class="masthead">
      <h1 class="masthead__name" lang="fr">Clinique<br>du petit<br>ruisseau</h1>
      <span class="masthead__dot" aria-hidden="true"></span>
      <p class="masthead__name" lang="en">Maple<br>Sprout<br>Clinic</p>
    </header>

    <div class="rule rule--top"></div>
    <div class="rule rule--bottom"></div>

    <footer class="contact">
      <p class="contact__address">2280 rue des Érables, Suite 210, Montréal, Qc&nbsp; H3A 1B2</p>
      <p class="contact__lines">Tél. (514) 555-0142 &nbsp;|&nbsp; Fax. (514) 555-0187</p>
    </footer>
  </main>
</body>
</html>
```